Entrepreneur needs a business card design

I need a business card to name my three companies, as well as contact information.
I'm open on design and color and it can be plain or complex. I'm open on colors but I think I prefer something somewhat formal but fun as well.
I'm open on whether the background is plain or has design in it. I don't have company logos.
Target Market(s)
Auto dealers, realtors and property managers
Industry/Entity Type
Business
Contact Information for Business Card
HALVERSEN FAMILY PROPERTIES, LLC
HALVERSEN PUBLISHING, LLC
MOTORVANE CONSULTING, LLC
Lee Halversen
2871 W. Tamarind Ave. #419
Boise, Idaho 83719-2056
208-514-3092
lee@halv3rn.com

```html
<!DOCTYPE html>
<html lang="en">
<head>
<meta charset="utf-8">
<title>Lee Halversen — Business Card</title>
<link rel="stylesheet" href="https://fonts.googleapis.com/css2?family=Merriweather:wght@700&family=Raleway:wght@300;400&display=swap">
<style>
  :root {
    --page: #f8fcfd;
    --card-top: #646769;
    --card-mid: #5a5d61;
    --card-deep: #232323;
    --card-bottom: #1e1e1e;
    --rule: #222325;
    --name: #ffffff;
    --company: #d3d5d8;
    --contact: #ffffff;
  }
  * { margin: 0; padding: 0; box-sizing: border-box; }
  html, body {
    width: 1200px;
    height: 720px;
    overflow: hidden;
    background: var(--page);
  }
  .card {
    position: absolute;
    left: 0;
    top: 30px;
    width: 1200px;
    height: 659px;
    background: linear-gradient(to bottom,
      var(--card-top) 0%,
      var(--card-mid) 30%,
      var(--card-deep) 68%,
      var(--card-bottom) 100%);
  }
  .owner-name {
    position: absolute;
    left: 0;
    width: 1200px;
    top: 62px;
    text-align: center;
    font-family: "Merriweather", Georgia, serif;
    font-weight: 700;
    font-size: 64px;
    line-height: 1;
    letter-spacing: 2px;
    color: var(--name);
  }
  .name-rule {
    position: absolute;
    left: 270px;
    top: 148px;
    width: 661px;
    height: 5px;
    background: var(--rule);
  }
  .company {
    position: absolute;
    top: 170px;
    width: 300px;
    text-align: center;
    font-family: "Raleway", Arial, sans-serif;
    font-weight: 400;
    font-size: 26px;
    line-height: 33px;
    letter-spacing: 1px;
    color: var(--company);
  }
  .company--properties { left: 181px; }
  .company--publishing { left: 445px; }
  .company--consulting { left: 709px; }
  .contact {
    position: absolute;
    left: 0;
    width: 1200px;
    top: 490px;
    text-align: center;
    font-family: "Raleway", Arial, sans-serif;
    font-weight: 400;
    font-size: 31px;
    line-height: 48px;
    letter-spacing: 4px;
    color: var(--contact);
  }
  .contact .sep { margin: 0 14px; }
</style>
</head>
<body>
  <div class="card">
    <h1 class="owner-name">LEE HALVERSEN</h1>
    <div class="name-rule"></div>

    <p class="company company--properties">Halversen Family<br>Properties, LLC</p>
    <p class="company company--publishing">Halversen<br>Publishing, LLC</p>
    <p class="company company--consulting">Motorvane<br>Consulting, LLC</p>

    <div class="contact">
      <p class="contact-line">83719-2056<span class="sep">|</span>208-514-3092</p>
      <p class="contact-line">lee@halv3rn.com</p>
      <p class="contact-line">2871<span class="sep">|</span>W.Tamarind Ave.<span class="sep">|</span>#419 Boise, Idaho</p>
    </div>
  </div>
</body>
</html>
```